Design a label for a dog shampoo names furbloom, the sell point of this series of shampoo is “just like wash your dogs with milk, not harm for your hand ”, the style could be gentle or professional or even amazing.

Use only 2 colors in the design job, the color of our logo could be changed, it depends on your whole page. Please design in CDR or ai.

update:
Pls do more change with the fonts when you design the front page, including title and details. Try more styles of fonts. Addition, this design will be printed on the bottle, no a label stick on it.
Updates

Do not put a real dog or animal on the page, Pay more attention to the types of fonts

Reason: Expect for more design idea.

Target Market(s)

people 20-30 years old who have dogs and cats at home

Industry/Entity Type

It Professional

Requirements
Nice to have
• It would be nice if you add some detail words in the design of the right side.

```html
<!DOCTYPE html>
<html lang="en">
<head>
<meta charset="utf-8">
<title>furbloom — Super-Conditioning &amp; Nutrient Shampoo</title>
<link href="https://fonts.googleapis.com/css2?family=Questrial&family=Arimo&display=swap" rel="stylesheet">
<style>
  :root {
    --green: #8cc63f;
    --green-light: #c4e08f;
    --green-pale: #e6f2d2;
    --green-deep: #6fa82c;
    --white: #ffffff;
  }
  html, body {
    margin: 0;
    padding: 0;
    width: 1200px;
    height: 2307px;
    overflow: hidden;
    background: var(--white);
  }
  .label {
    position: relative;
    width: 1200px;
    height: 2307px;
    overflow: hidden;
    background: var(--white);
    font-family: "Questrial", sans-serif;
  }
  .swooshes {
    position: absolute;
    inset: 0;
  }
  .brand {
    position: absolute;
    left: 760px;
    top: 205px;
    width: 380px;
    height: 120px;
    display: flex;
    align-items: center;
    justify-content: center;
    gap: 18px;
    color: var(--green);
    font-family: "Questrial", sans-serif;
    font-size: 78px;
    line-height: 1;
    letter-spacing: 1px;
  }
  .brand-dot {
    width: 30px;
    height: 30px;
    border-radius: 50%;
    background: var(--green);
    flex: none;
  }
  .mascot-area {
    position: absolute;
    left: 275px;
    top: 600px;
    width: 900px;
    height: 960px;
    border-radius: 46% 46% 40% 40%;
    background: radial-gradient(ellipse at 55% 45%, var(--green-pale) 0%, #f3f9ea 55%, rgba(255,255,255,0) 75%);
  }
  .product-banner {
    position: absolute;
    left: 200px;
    top: 1625px;
    width: 915px;
    height: 235px;
    background: var(--green);
    border-radius: 70px 0 70px 0;
    color: var(--white);
    text-align: center;
    box-sizing: border-box;
    padding-top: 24px;
  }
  .product-name {
    margin: 0;
    font-family: "Questrial", sans-serif;
    font-weight: 400;
    font-size: 60px;
    line-height: 66px;
    letter-spacing: 3px;
  }
  .product-claim {
    display: inline-block;
    margin-top: 14px;
    padding: 4px 22px;
    border: 3px solid var(--white);
    border-radius: 30px;
    font-size: 30px;
    letter-spacing: 1px;
    line-height: 34px;
  }
  .volume {
    position: absolute;
    left: 740px;
    top: 2060px;
    margin: 0;
    color: var(--green);
    font-family: "Arimo", sans-serif;
    font-size: 50px;
    line-height: 1;
  }
</style>
</head>
<body>
<main class="label">
  <svg class="swooshes" width="1200" height="2307" viewBox="0 0 1200 2307" aria-hidden="true">
    <defs>
      <linearGradient id="leftBand" x1="0" y1="0" x2="1" y2="1">
        <stop offset="0" stop-color="#8cc63f"/>
        <stop offset="0.5" stop-color="#c4e08f"/>
        <stop offset="1" stop-color="#8cc63f"/>
      </linearGradient>
      <linearGradient id="topBand" x1="0" y1="0" x2="1" y2="1">
        <stop offset="0" stop-color="#e6f2d2"/>
        <stop offset="1" stop-color="#8cc63f"/>
      </linearGradient>
    </defs>
    <!-- left and bottom sweep -->
    <path d="M0,0 L360,0 C140,320 60,900 160,1500 C250,1930 640,2200 1200,2240 L1200,2307 L0,2307 Z" fill="url(#leftBand)"/>
    <path d="M0,0 L250,0 C60,350 0,900 70,1450 C140,1950 500,2250 900,2307 L0,2307 Z" fill="#8cc63f" opacity="0.55"/>
    <path d="M300,0 C100,330 30,900 130,1500 C220,1960 620,2230 1200,2270" fill="none" stroke="#ffffff" stroke-width="6" opacity="0.9"/>
    <path d="M200,0 C40,380 -10,950 90,1550 C190,2050 560,2280 900,2307" fill="none" stroke="#ffffff" stroke-width="3" opacity="0.8"/>
    <path d="M120,0 C0,420 -30,1000 40,1600" fill="none" stroke="#ffffff" stroke-width="3" opacity="0.7"/>
    <!-- bottom right accent -->
    <path d="M420,2307 C700,2230 1000,2180 1200,2080 L1200,2307 Z" fill="#c4e08f" opacity="0.7"/>
    <path d="M600,2307 C850,2250 1050,2200 1200,2140" fill="none" stroke="#ffffff" stroke-width="4"/>
    <!-- top right sweep -->
    <path d="M560,0 L780,0 C930,60 1100,160 1200,270 L1200,340 C1050,190 810,70 560,0 Z" fill="url(#topBand)"/>
    <path d="M640,0 C860,60 1060,170 1200,300" fill="none" stroke="#ffffff" stroke-width="4"/>
  </svg>

  <div class="brand">
    <span class="brand-dot"></span>
    <span class="brand-name">furbloom</span>
  </div>

  <div class="mascot-area" role="img" aria-label="Line illustration of a sitting puppy in green tones"></div>

  <section class="product-banner">
    <h1 class="product-name">SUPER-CONDITIONING<br>&amp; NUTRIENT SHAMPOO</h1>
    <span class="product-claim">MOISTURE RICH, SMOOTH AND SILKY</span>
  </section>

  <p class="volume">1000 ML</p>
</main>
</body>
</html>
```